Electrical company business card design.

Hi, were an electrical company in Auckland New Zealand called Quarneth Ltd. We focus mainly on high end residential and commercial so the card would be targeted towards that.
The card will be for myself, i am the director of the company.
Name: Derek Olstow
Position: Director/electrician
Phone: 021 387 9415
Email: derek@quarneth.co.nz
Location: Auckland
As for colors the the blue color in the logo is preferred, i also don't mind a black background option.
Target Market(s)
High end residential and commercial
Industry/Entity Type
Electrician
Contact Information for Business Card
Name: Derek Olstow Position: Director/Electrician Phone: 021 387 9415, Email: derek@quarneth.co.nz, Location: Auckland

```html
<!DOCTYPE html>
<html lang="en">
<head>
<meta charset="utf-8">
<title>Quarneth Ltd — Business Card</title>
<link href="https://fonts.googleapis.com/css2?family=Montserrat:wght@400;500;800&display=swap" rel="stylesheet">
<style>
  :root {
    --stage: #2b2b2d;
    --card: #141414;
    --brand-blue: #1a73c9;
    --brand-blue-light: #2a95e6;
    --slate: #4c535b;
    --slate-light: #8b929a;
    --ink: #f2f2f2;
  }
  * { box-sizing: border-box; margin: 0; padding: 0; }
  html, body { width: 1200px; height: 689px; overflow: hidden; }
  body {
    background: var(--stage);
    font-family: "Montserrat", sans-serif;
    position: relative;
  }
  .card {
    position: absolute;
    top: 190px;
    width: 540px;
    height: 309px;
    border-radius: 22px;
    background: var(--card);
    box-shadow: 0 18px 40px rgba(0,0,0,.45);
    overflow: hidden;
  }
  .card--front { left: 40px; }
  .card--back { left: 620px; }

  /* Front */
  .front-pattern {
    position: absolute; inset: 0;
    background: linear-gradient(115deg, #b9b9b9 0%, #6e6e6e 22%, #2a2a2a 45%, #151515 70%, #111 100%);
  }
  .front-brand {
    position: absolute;
    left: 0; right: 0; top: 50%;
    transform: translateY(-50%);
    text-align: center;
  }
  .wordmark {
    font-weight: 500;
    font-size: 50px;
    letter-spacing: 2px;
    color: var(--slate-light);
    line-height: 1;
  }

  /* Back */
  .back-brand {
    position: absolute;
    left: 34px; top: 146px;
    width: 244px;
  }
  .back-brand .wordmark { font-size: 38px; color: var(--slate); letter-spacing: 1.5px; }
  .divider {
    position: absolute;
    left: 292px; top: 44px;
    width: 1.5px; height: 220px;
    background: linear-gradient(var(--brand-blue), var(--brand-blue-light));
  }
  .contact {
    position: absolute;
    left: 312px; top: 58px;
    color: var(--ink);
  }
  .contact__name {
    font-weight: 800;
    font-size: 25px;
    color: var(--brand-blue);
    line-height: 1.1;
  }
  .contact__role { font-size: 14px; margin-top: 4px; }
  .contact__city { font-size: 14px; margin-top: 26px; }
  .contact__list { list-style: none; margin-top: 22px; }
  .contact__item {
    display: flex; align-items: center; gap: 8px;
    font-size: 14px; margin-bottom: 6px;
  }
  .contact__icon { width: 12px; height: 12px; fill: var(--brand-blue); flex: none; }
</style>
</head>
<body>

<section class="card card--front">
  <div class="front-pattern" role="img" aria-label="Repeating brand symbol pattern fading from silver to black"></div>
  <div class="front-brand">
    <div class="wordmark">QUARNETH</div>
  </div>
</section>

<section class="card card--back">
  <div class="back-brand">
    <div class="wordmark">QUARNETH</div>
  </div>
  <div class="divider"></div>
  <div class="contact">
    <div class="contact__name">Derek Olstow</div>
    <div class="contact__role">Director/Electrician</div>
    <div class="contact__city">Auckland</div>
    <ul class="contact__list">
      <li class="contact__item">
        <svg class="contact__icon" viewBox="0 0 24 24" aria-hidden="true"><path d="M6.6 10.8a15.1 15.1 0 0 0 6.6 6.6l2.2-2.2c.3-.3.7-.4 1-.2 1.1.4 2.3.6 3.6.6.6 0 1 .4 1 1V20c0 .6-.4 1-1 1C10.6 21 3 13.4 3 4c0-.6.4-1 1-1h3.5c.6 0 1 .4 1 1 0 1.3.2 2.5.6 3.6.1.3 0 .7-.2 1z"/></svg>
        <span>021 387 9415</span>
      </li>
      <li class="contact__item">
        <svg class="contact__icon" viewBox="0 0 24 24" aria-hidden="true"><path d="M2 5h20v14H2z M2 5l10 8 10-8" fill="none" stroke="#1a73c9" stroke-width="2.4"/><path d="M2 5h20l-10 8z"/></svg>
        <span>derek@quarneth.co.nz</span>
      </li>
    </ul>
  </div>
</section>

</body>
</html>
```